M Zyvantics Buisness Cards

I need a technology focused clean business card for my employees. I have attached out logo to include in the mocks. We're a modern tech consulting firm that drives to interface humanity with technology in a truly cohesive fashion.

```html
<!DOCTYPE html>
<html lang="en">
<head>
<meta charset="utf-8">
<title>M Zyvantics Business Cards</title>
<link rel="stylesheet" href="https://fonts.googleapis.com/css2?family=Work+Sans:wght@400;500;600&display=swap">
<style>
  :root {
    --backdrop: #2a2a2b;
    --card: #1b1b1c;
    --card-edge: #232324;
    --ink-white: #f4f4f4;
    --ink-soft: #d9d9d9;
    --brand-blue: #1a7fd0;
    --silver-light: #e6e6e6;
    --silver-dark: #4a4a4b;
  }
  * { margin: 0; padding: 0; box-sizing: border-box; }
  html, body { width: 1200px; height: 900px; overflow: hidden; }
  body {
    background: var(--backdrop);
    font-family: "Work Sans", Arial, sans-serif;
    position: relative;
  }
  .card {
    position: absolute;
    left: 250px;
    width: 700px;
    height: 400px;
    background: var(--card);
    border: 1px solid var(--card-edge);
    box-shadow: 0 14px 30px rgba(0,0,0,0.45);
    overflow: hidden;
  }
  .card-back { top: 40px; }
  .card-front { top: 465px; }

  .back-wordmark {
    position: absolute;
    inset: 0;
    display: flex;
    align-items: center;
    justify-content: center;
    gap: 18px;
    font-size: 62px;
    font-weight: 600;
    color: #8d8d8e;
    letter-spacing: 1px;
  }
  .back-wordmark .mark-dot {
    width: 56px; height: 56px;
    border-radius: 50%;
    background: #5e5e5f;
  }

  .front-wordmark {
    position: absolute;
    left: 44px; top: 40px;
    display: flex;
    align-items: center;
    gap: 14px;
    font-size: 44px;
    font-weight: 600;
    color: var(--ink-white);
  }
  .front-wordmark .mark-dot {
    width: 46px; height: 46px;
    border-radius: 50%;
    background: var(--brand-blue);
  }

  .contact-block {
    position: absolute;
    left: 60px; top: 148px;
    color: var(--ink-soft);
  }
  .person-name {
    font-size: 28px;
    font-weight: 500;
    color: var(--brand-blue);
    letter-spacing: 0.5px;
    line-height: 1;
  }
  .person-role {
    font-size: 17px;
    color: var(--ink-white);
    margin-top: 4px;
  }
  .address {
    font-size: 18px;
    line-height: 1.3;
    margin-top: 22px;
    color: var(--ink-white);
  }
  .contact-list {
    list-style: none;
    margin-top: 14px;
    font-size: 19px;
    line-height: 1.3;
    color: var(--ink-white);
  }
  .contact-list li { display: flex; align-items: center; gap: 10px; }
  .contact-list svg { width: 13px; height: 13px; flex: none; }

  .emblem {
    position: absolute;
    right: 70px; top: 60px;
    width: 320px; height: 320px;
    border-radius: 50%;
    background: linear-gradient(115deg, var(--silver-dark) 0%, #8a8a8b 55%, var(--silver-light) 100%);
    opacity: 0.85;
  }
</style>
</head>
<body>
  <section class="card card-back" aria-label="Card back">
    <div class="back-wordmark"><span class="mark-dot"></span><span>M Zyvantics</span></div>
  </section>

  <section class="card card-front" aria-label="Card front">
    <div class="front-wordmark"><span class="mark-dot"></span><span>M Zyvantics</span></div>

    <div class="contact-block">
      <p class="person-name">DANA WHITLOW</p>
      <p class="person-role">Director</p>
      <p class="address">2250 Orchard Vale Rd<br>Larkspur, CA 94939-1180</p>
      <ul class="contact-list">
        <li>
          <svg viewBox="0 0 16 16" aria-hidden="true"><path d="M4 1.5c.6 0 1 .3 1.2.8l.9 2.2c.2.5 0 1-.4 1.3l-1 .7c.7 1.6 2 2.9 3.6 3.6l.7-1c.3-.4.8-.6 1.3-.4l2.2.9c.5.2.8.6.8 1.2v1.7c0 .8-.6 1.4-1.4 1.4C6.6 13.9 2.1 9.4 2.1 2.9c0-.8.6-1.4 1.4-1.4z" fill="var(--brand-blue)"/></svg>
          <span>555-204-7731</span>
        </li>
        <li>
          <svg viewBox="0 0 16 16" aria-hidden="true"><rect x="1.5" y="3.5" width="13" height="9" fill="none" stroke="var(--brand-blue)" stroke-width="1.4"/><path d="M1.5 3.5l6.5 5 6.5-5" fill="none" stroke="var(--brand-blue)" stroke-width="1.4"/></svg>
          <span>info@mzyvantics.com</span>
        </li>
        <li>
          <svg viewBox="0 0 16 16" aria-hidden="true"><circle cx="8" cy="8" r="6.3" fill="none" stroke="var(--brand-blue)" stroke-width="1.3"/><ellipse cx="8" cy="8" rx="2.8" ry="6.3" fill="none" stroke="var(--brand-blue)" stroke-width="1.1"/><path d="M1.7 8h12.6" stroke="var(--brand-blue)" stroke-width="1.1"/></svg>
          <span>www.mzyvantics.com</span>
        </li>
      </ul>
    </div>

    <div class="emblem" role="img" aria-label="Large silver brand emblem area"></div>
  </section>
</body>
</html>
```